W need a Menu Board designed for a" make your own poke bowl" and Sushi Menu. We would like our logo & Colors to be intergraded with the menu . Also will need to be able to adjust the pricing in the future as needed.

```html
<!DOCTYPE html>
<html lang="en">
<head>
<meta charset="utf-8">
<title>Tideline – Build Your Own Poke Bowl &amp; Sushi Menu</title>
<link rel="stylesheet" href="https://fonts.googleapis.com/css2?family=Bebas+Neue&family=Montserrat:wght@400;500;600;700;800&display=swap">
<style>
:root{
  --blue:#1f4d9e;
  --blue-soft:#8fb0dc;
  --blue-pale:#c9daf0;
  --ink:#1e1e1e;
  --muted:#7a7a7a;
  --paper:#ffffff;
  --stage:#e9ebee;
  --blush:#f1d3d6;
}
*{box-sizing:border-box;margin:0;padding:0}
html,body{width:1200px;height:3545px;overflow:hidden;background:var(--stage)}
body{font-family:"Montserrat",sans-serif;color:var(--ink);position:relative}

.page{position:absolute;left:80px;width:1040px;height:1344px;background:var(--paper);box-shadow:0 6px 22px rgba(0,0,0,.18);overflow:hidden}
.page--one{top:328px}
.page--two{top:1888px}

.brand{position:absolute;left:45px;top:60px;width:330px;text-align:left}
.brand__name{font-family:"Montserrat",sans-serif;font-weight:800;font-size:62px;letter-spacing:2px;color:var(--blue);line-height:1}
.brand__tag{margin-top:16px;font-weight:700;font-size:17px;letter-spacing:4px;color:var(--blue-soft)}

.title{position:absolute;left:464px;top:38px;width:540px}
.title__kicker{font-weight:800;font-size:40px;color:var(--ink);text-align:center;padding-left:40px;letter-spacing:.5px}
.title__banner{margin-top:10px;height:90px;background:var(--blue);clip-path:polygon(4% 0,100% 0,96% 100%,0 100%);display:flex;align-items:center;justify-content:center;font-family:"Bebas Neue",sans-serif;font-size:76px;color:#fff;letter-spacing:1px;padding-top:6px}

.dots-deco{position:absolute;right:6px;top:6px;width:130px;height:70px;background:var(--blush);opacity:.55;border-radius:6px}

.col{position:absolute}
.col--left{left:45px;width:423px}
.col--right{left:564px;width:433px}

.art{position:absolute;border-radius:14px}
.art--sushi{background:linear-gradient(90deg,#a9c96a,#f2a25c 55%,#e8e8e8)}
.art--fish{background:linear-gradient(90deg,#d9e3f2,#d8443a 50%,#d9e3f2)}
.art--bowls{background:linear-gradient(90deg,#c7d86a,#f0b08a 40%,#e7e7e7 60%,#3c6bb0)}
.art--veg{background:linear-gradient(90deg,#f1d3d6,#d9533a 45%,#7bb04a)}
.art--sauce{background:linear-gradient(90deg,#f1d3d6,#c9382a 40%,#e6a532 75%,#d86a2a)}
.art--soup{background:radial-gradient(circle at 70% 50%,#e05a2a,#f1d3d6 70%)}
.art--crunch{background:linear-gradient(90deg,#3b5b3b,#9cc86a 50%,#f1d3d6)}
.art--fruit{background:linear-gradient(90deg,#f0a64a,#6b8b3a 50%,#c99a45)}
.art--platter{background:linear-gradient(135deg,#f4f4f4,#e8c65a 45%,#ef8c6a 70%,#f4f4f4)}

.heading{position:absolute;left:0;right:0;border-bottom:3px solid var(--blue-soft);padding-bottom:6px}
.heading__main{font-weight:700;font-size:27px;color:var(--blue);letter-spacing:.5px}
.heading__sub{display:block;font-weight:500;font-size:19px;color:var(--ink);line-height:1.15}
.heading--small .heading__main{font-size:20px}
.heading--centered{text-align:center}

.list{position:absolute;left:0;right:0;list-style:none;display:flex;flex-direction:column}
.row{display:flex;align-items:flex-end;font-weight:500;font-size:20px;line-height:24px;height:32px;padding-bottom:4px}
.row--tall{height:60px}
.row__name{white-space:nowrap}
.row__dots{flex:1;border-bottom:2px dotted #555;margin:0 4px 6px}
.row__price{font-weight:700;white-space:nowrap}
.row--note{height:auto;flex-wrap:wrap;padding-top:6px}
.row__note{flex-basis:100%;font-size:12.5px;line-height:15px;color:var(--muted);font-weight:500;max-width:300px}

.pill{position:absolute;left:70px;top:789px;padding:10px 34px;background:var(--blue-pale);border-radius:40px 30px 40px 20px;font-weight:500;font-size:20px}
.pill strong{color:var(--blue);font-weight:700}

.waves{position:absolute;left:0;right:0;bottom:8px;height:20px;background:linear-gradient(90deg,var(--blue-pale),var(--blue-soft),var(--blue-pale))}
</style>
</head>
<body>

<section class="page page--one">
  <div class="dots-deco" role="img" aria-label="Cluster of small pink decorative circles"></div>
  <header>
    <div class="brand">
      <div class="brand__name">TIDELINE</div>
      <div class="brand__tag">SPECIALTY FISH MARKET</div>
    </div>
    <div class="title">
      <div class="title__kicker">BUILD YOUR OWN</div>
      <div class="title__banner">POKE BOWL &amp; SUSHI</div>
    </div>
  </header>

  <div class="col col--left">
    <div class="art art--sushi" style="left:0;top:208px;width:423px;height:84px" role="img" aria-label="Illustration of sushi rolls and chopsticks"></div>
    <div class="heading" style="top:292px;padding-left:92px"><span class="heading__main">SUSHI ROLLS</span></div>
    <ul class="list" style="top:352px">
      <li class="row"><span class="row__name">TUNA TARTAR</span><span class="row__dots"></span><span class="row__price">$24.99</span></li>
      <li class="row"><span class="row__name">SALMON TARTAR</span><span class="row__dots"></span><span class="row__price">$22.99</span></li>
      <li class="row"><span class="row__name">SALMON TOWER</span><span class="row__dots"></span><span class="row__price">$16.99</span></li>
      <li class="row"><span class="row__name">KANI SALAD</span><span class="row__dots"></span><span class="row__price">$18.99</span></li>
      <li class="row"><span class="row__name">TUNA TATAKI</span><span class="row__dots"></span><span class="row__price">$------</span></li>
      <li class="row"><span class="row__name">CALIFORNIA ROLL</span><span class="row__dots"></span><span class="row__price">$9.99</span></li>
      <li class="row"><span class="row__name">AVOCADO ROLL</span><span class="row__dots"></span><span class="row__price">$7.99</span></li>
      <li class="row"><span class="row__name">TUNA ROLL (SMALL)</span><span class="row__dots"></span><span class="row__price">$9.99</span></li>
      <li class="row"><span class="row__name">SALMON ROLL (SMALL)</span><span class="row__dots"></span><span class="row__price">$9.99</span></li>
      <li class="row"><span class="row__name">CUCUMBER ROLL</span><span class="row__dots"></span><span class="row__price">$7.99</span></li>
      <li class="row"><span class="row__name">VEGGIE ROLL</span><span class="row__dots"></span><span class="row__price">$9.99</span></li>
      <li class="row"><span class="row__name">VEGGIE ROLL</span><span class="row__dots"></span><span class="row__price">$9.99</span></li>
      <li class="row row--tall"><span class="row__name">SALMON<br>AVOCADO ROLL</span><span class="row__dots"></span><span class="row__price">$9.99</span></li>
      <li class="row row--tall"><span class="row__name">SALMON AVOCADO<br>W/ SALMON ON TOP</span><span class="row__dots"></span><span class="row__price">$14.99</span></li>
      <li class="row row--tall"><span class="row__name">SALMON AVOCADO<br>W/ TUNA ON TOP</span><span class="row__dots"></span><span class="row__price">$14.99</span></li>
      <li class="row row--tall"><span class="row__name">TUNA AVOCADO<br>W/ TUNA ON TOP</span><span class="row__dots"></span><span class="row__price">$14.99</span></li>
      <li class="row row--tall"><span class="row__name">TUNA AVOCADO<br>W/ SALMON ON TOP</span><span class="row__dots"></span><span class="row__price">$14.99</span></li>
      <li class="row"><span class="row__name">SPICY TUNA ROLL</span><span class="row__dots"></span><span class="row__price">$9.99</span></li>
      <li class="row row--note"><span class="row__name">HARBOR ROLL</span><span class="row__dots"></span><span class="row__price">$14.99</span><span class="row__note">INSIDE OUT W/ CRAB, CUCUMBER, AVOCADO &amp; CRISPY FLAKES TOPPED W/ SALMON &amp; A SWEET SOY GLAZE</span></li>
      <li class="row row--note"><span class="row__name">EMBER ROLL</span><span class="row__dots"></span><span class="row__price">$15.99</span><span class="row__note">INSIDE OUT W/ CRAB, CUCUMBER &amp; HERBS TOPPED W/ YELLOWTAIL, JALAPENO &amp; A LIGHT CITRUS HERB DRESSING</span></li>
    </ul>
  </div>

  <div class="col col--right">
    <div class="art art--fish" style="left:0;top:210px;width:433px;height:90px" role="img" aria-label="Illustration of nigiri pieces, fish roe sushi and fish icons"></div>
    <div class="heading heading--centered" style="top:292px"><span class="heading__main">NEGRI</span></div>
    <ul class="list" style="top:352px">
      <li class="row"><span class="row__name">SALMON</span><span class="row__dots"></span><span class="row__price">$00.00</span></li>
      <li class="row"><span class="row__name">AHI</span><span class="row__dots"></span><span class="row__price">$00.00</span></li>
      <li class="row"><span class="row__name">WAHOO</span><span class="row__dots"></span><span class="row__price">$00.00</span></li>
      <li class="row"><span class="row__name">HAMACHI</span><span class="row__dots"></span><span class="row__price">$00.00</span></li>
      <li class="row"><span class="row__name">TORO</span><span class="row__dots"></span><span class="row__price">$00.00</span></li>
    </ul>
    <div class="art art--bowls" style="left:0;top:527px;width:433px;height:170px" role="img" aria-label="Illustration of two poke bowls with chopsticks and soy sauce"></div>
    <div class="heading" style="top:700px"><span class="heading__main">POKE BOWLS</span></div>
    <div class="pill">STARTING PRICE | <strong>$15.99</strong></div>
    <div class="heading heading--small" style="top:838px;padding-left:8px"><span class="heading__main">CHOICE 1 BASE:</span></div>
    <ul class="list" style="top:876px;padding-left:8px">
      <li class="row"><span class="row__name">WHITE RICE</span><span class="row__dots"></span><span class="row__price">$00.00</span></li>
      <li class="row"><span class="row__name">BROWN RICE</span><span class="row__dots"></span><span class="row__price">$00.00</span></li>
      <li class="row"><span class="row__name">QUINOA</span><span class="row__dots"></span><span class="row__price">$00.00</span></li>
      <li class="row"><span class="row__name">ZUCCHINI NOODLES</span><span class="row__dots"></span><span class="row__price">$00.00</span></li>
      <li class="row"><span class="row__name">LETTUCE</span><span class="row__dots"></span><span class="row__price">$00.00</span></li>
    </ul>
    <div class="heading heading--small" style="top:1050px;padding-left:8px"><span class="heading__main">CHOICE 1 PROTEIN:</span></div>
    <ul class="list" style="top:1088px;padding-left:8px">
      <li class="row"><span class="row__name">TUNA POKE</span><span class="row__dots"></span><span class="row__price">$00.00</span></li>
      <li class="row"><span class="row__name">SALMON POKE</span><span class="row__dots"></span><span class="row__price">$00.00</span></li>
      <li class="row"><span class="row__name">SPICY TUNA</span><span class="row__dots"></span><span class="row__price">$00.00</span></li>
      <li class="row"><span class="row__name">SPICY SALMON</span><span class="row__dots"></span><span class="row__price">$00.00</span></li>
      <li class="row"><span class="row__name">KANI</span><span class="row__dots"></span><span class="row__price">$00.00</span></li>
      <li class="row"><span class="row__name">WAHOO</span><span class="row__dots"></span><span class="row__price">$00.00</span></li>
    </ul>
  </div>
  <div class="waves" role="img" aria-label="Band of small blue wave ornaments"></div>
</section>

<section class="page page--two">
  <div class="dots-deco" role="img" aria-label="Cluster of small pink decorative circles"></div>
  <header>
    <div class="brand">
      <div class="brand__name">TIDELINE</div>
      <div class="brand__tag">SPECIALTY FISH MARKET</div>
    </div>
    <div class="title">
      <div class="title__kicker">BUILD YOUR OWN</div>
      <div class="title__banner">POKE BOWL &amp; SUSHI</div>
    </div>
  </header>

  <div class="col col--left">
    <div class="art art--veg" style="left:150px;top:208px;width:273px;height:118px" role="img" aria-label="Illustration of peppers and edamame"></div>
    <div class="heading" style="top:286px;width:150px;right:auto;border-bottom:none"><span class="heading__sub">CHOICE 4</span><span class="heading__main" style="font-size:20px">TOPPINGS:</span></div>
    <div class="heading" style="top:336px;border-bottom-width:3px;padding:0"></div>
    <ul class="list" style="top:350px">
      <li class="row"><span class="row__name">ASIAN SLAW</span><span class="row__dots"></span><span class="row__price">$--------</span></li>
      <li class="row"><span class="row__name">EDAMAME</span><span class="row__dots"></span><span class="row__price">$--------</span></li>
      <li class="row"><span class="row__name">RED ONION</span><span class="row__dots"></span><span class="row__price">$--------</span></li>
      <li class="row"><span class="row__name">RED CABBAGE</span><span class="row__dots"></span><span class="row__price">$--------</span></li>
      <li class="row"><span class="row__name">JALAPENO</span><span class="row__dots"></span><span class="row__price">$--------</span></li>
      <li class="row"><span class="row__name">SCALLIONS</span><span class="row__dots"></span><span class="row__price">$--------</span></li>
      <li class="row"><span class="row__name">CARROT</span><span class="row__dots"></span><span class="row__price">$--------</span></li>
      <li class="row"><span class="row__name">RADISH</span><span class="row__dots"></span><span class="row__price">$--------</span></li>
      <li class="row"><span class="row__name">CUCUMBER</span><span class="row__dots"></span><span class="row__price">$--------</span></li>
      <li class="row"><span class="row__name">TOMATO</span><span class="row__dots"></span><span class="row__price">$--------</span></li>
      <li class="row"><span class="row__name">SPROUT</span><span class="row__dots"></span><span class="row__price">$--------</span></li>
      <li class="row"><span class="row__name">CILANTRO</span><span class="row__dots"></span><span class="row__price">$--------</span></li>
      <li class="row"><span class="row__name">PICKLED GINGER</span><span class="row__dots"></span><span class="row__price">$--------</span></li>
    </ul>
    <div class="art art--crunch" style="left:228px;top:790px;width:195px;height:66px" role="img" aria-label="Illustration of nori-wrapped avocado roll"></div>
    <div class="heading heading--small" style="top:830px"><span class="heading__sub" style="display:inline;font-size:20px">CHOICE 1 </span><span class="heading__main">CRUNCH:</span></div>
    <ul class="list" style="top:872px">
      <li class="row"><span class="row__name">TEMPURA FLAKES</span><span class="row__dots"></span><span class="row__price">$--------</span></li>
      <li class="row row--tall" style="height:58px"><span class="row__name">TOASTED<br>SHREDDED NORI</span><span class="row__dots"></span><span class="row__price">$--------</span></li>
      <li class="row"><span class="row__name">TOASTED SESAME</span><span class="row__dots"></span><span class="row__price">$--------</span></li>
    </ul>
    <div class="art art--fruit" style="left:338px;top:1010px;width:160px;height:260px;border-radius:20px" role="img" aria-label="Illustration of mango, avocado and pineapple"></div>
    <div class="heading heading--small" style="top:1060px;right:95px"><span class="heading__sub" style="display:inline;font-size:20px">PREMIUM </span><span class="heading__main">TOPPINGS:</span></div>
    <ul class="list" style="top:1102px;right:95px">
      <li class="row"><span class="row__name">AVOCADO</span><span class="row__dots"></span><span class="row__price">$2.00</span></li>
      <li class="row"><span class="row__name">KANI SALAD</span><span class="row__dots"></span><span class="row__price">$1.00</span></li>
      <li class="row"><span class="row__name">WAKAME</span><span class="row__dots"></span><span class="row__price">$1.00</span></li>
      <li class="row"><span class="row__name">MANGO</span><span class="row__dots"></span><span class="row__price">$1.00</span></li>
      <li class="row"><span class="row__name">PINEAPPLE</span><span class="row__dots"></span><span class="row__price">$1.00</span></li>
    </ul>
  </div>

  <div class="col col--right">
    <div class="art art--sauce" style="left:0;top:200px;width:433px;height:124px" role="img" aria-label="Illustration of sauce bottles pouring"></div>
    <div class="heading heading--small" style="top:306px"><span class="heading__main">SAUCES:</span></div>
    <ul class="list" style="top:350px">
      <li class="row"><span class="row__name">SPICY MAYO</span><span class="row__dots"></span><span class="row__price">$-------</span></li>
      <li class="row"><span class="row__name">SWEET CHILI</span><span class="row__dots"></span><span class="row__price">$-------</span></li>
      <li class="row"><span class="row__name">SRIRACHA</span><span class="row__dots"></span><span class="row__price">$-------</span></li>
      <li class="row"><span class="row__name">PONZU</span><span class="row__dots"></span><span class="row__price">$-------</span></li>
      <li class="row"><span class="row__name">EEL SAUCE</span><span class="row__dots"></span><span class="row__price">$-------</span></li>
      <li class="row row--tall" style="height:58px"><span class="row__name">CILANTRO GARLIC<br>AIOLI</span><span class="row__dots"></span><span class="row__price">$-------</span></li>
      <li class="row"><span class="row__name">BASIL AIOLI</span><span class="row__dots"></span><span class="row__price">$-------</span></li>
      <li class="row"><span class="row__name">SESAME GINGER</span><span class="row__dots"></span><span class="row__price">$-------</span></li>
      <li class="row row--tall" style="height:58px"><span class="row__name">CARROT HONEY<br>GINGER</span><span class="row__dots"></span><span class="row__price">$-------</span></li>
    </ul>
    <div class="art art--soup" style="left:210px;top:700px;width:223px;height:104px" role="img" aria-label="Illustration of soup bowl and small sauce dishes"></div>
    <div class="heading" style="top:752px;right:0"><span class="heading__sub">ADDITIONAL</span><span class="heading__main" style="font-size:20px">PROTEIN SCOOP:</span></div>
    <ul class="list" style="top:822px;right:10px">
      <li class="row"><span class="row__name">TUNA POKE</span><span class="row__dots"></span><span class="row__price">$4.00</span></li>
      <li class="row"><span class="row__name">SALMON POKE</span><span class="row__dots"></span><span class="row__price">$4.00</span></li>
      <li class="row"><span class="row__name">SPICY TUNA</span><span class="row__dots"></span><span class="row__price">$4.00</span></li>
      <li class="row"><span class="row__name">SPICY SALMON</span><span class="row__dots"></span><span class="row__price">$4.00</span></li>
      <li class="row"><span class="row__name">KANI</span><span class="row__dots"></span><span class="row__price">$4.00</span></li>
    </ul>
    <div class="art art--platter" style="left:40px;top:1000px;width:393px;height:270px" role="img" aria-label="Illustration of a wooden sushi platter with rolls, sashimi and soup"></div>
  </div>
  <div class="waves" role="img" aria-label="Band of small blue wave ornaments"></div>
</section>

</body>
</html>
```